Flyer for spiritual retreat (yoga, meditation, reiki, raw food)

I would like a flyer to promote my upcoming retreat and a matching Facebook banner.

The name of the retreat is "Blossomreach Within" and the tagline is "retreat into you"

The activities in the retreat include daily meditation, ecstatic dance, spiritual development workshops on intuition, energy healing etc and a reiki session is included.

I would like a flyer designed to promote this, something that is editable as I will be running this multiple times and will need to adjust the flyer to add the dates etc each time.

edit: add that here will be fully catered raw food and juices, and that the retreat price includes all accomodation, meals and workshops.

Please contact me if you need further info. Please also visit my website www.marniekovac-studio.com and www.friendhub-sample.com/tuvelanook to see my current events and promotions.

Thank you,

Marnie

Reason: Hi all, thank you all for your submissions. Apologies as I am traveling and do not have much access to internet and will review your submissions and provide feedback as soon as possible. Kind regards, Marnie.

Target Market(s)

People who like meditation, yoga, fans of ronan feldspar and mervin okoro, those interested in personal and spiritual development.

Industry/Entity Type

Health And Wellness

Requirements
Must have
• Please put the included reiki session as as added bonus. Something like "BONUS 30 minute reiki healing session" in a little star/banner/something that stands out.
• Please emphasise the "light" part of Blossomreach as I am going for a play on words between in the light and enlightenment.
• Please include placeholder text for place, location, time
• Placeholder for price
• My name (see attached file - can change colour to suit) and website (www.marniekovac-studio.com)
Nice to have
• I prefer rounded designs, curves rather than block designs.
Should not have
• Tuvela Nook logo

```html
<!DOCTYPE html>
<html lang="en">
<head>
<meta charset="utf-8">
<title>Blossomreach Within – Retreat Flyer</title>
<link rel="stylesheet" href="https://fonts.googleapis.com/css2?family=Lobster&family=Roboto+Condensed:ital,wght@1,700&family=Roboto:ital,wght@0,400;1,400;1,700&display=swap">
<style>
  :root{
    --stage:#e4e6ea;
    --ink:#1b1d21;
    --panel:#26282c;
    --sky:#43c2f2;
    --sky-deep:#16a7e3;
    --paper-shade:#dcdcdc;
    --white:#ffffff;
    --ring:#e3e5e8;
  }
  html,body{margin:0;padding:0;width:1200px;height:1200px;overflow:hidden;background:var(--stage);}
  .flyer{position:absolute;left:183px;top:13px;width:834px;height:1174px;display:block;}
  .brand-name{font-family:"Roboto",sans-serif;font-weight:400;font-size:46px;fill:#3a3c40;}
  .tagline{font-family:"Lobster",cursive;font-size:70px;fill:var(--white);}
  .headline{font-family:"Roboto Condensed",sans-serif;font-style:italic;font-weight:700;font-size:80px;}
  .headline--dark{fill:var(--ink);}
  .headline--light{fill:var(--white);}
  .cta-label{font-family:"Roboto Condensed",sans-serif;font-style:italic;font-weight:700;font-size:34px;fill:var(--white);}
  .details{font-family:"Roboto",sans-serif;font-style:italic;font-size:15.5px;fill:var(--ink);}
  .event-info{font-family:"Roboto",sans-serif;font-style:italic;font-weight:700;font-size:15.5px;fill:var(--sky-deep);}
  .bonus-title{font-family:"Roboto Condensed",sans-serif;font-style:italic;font-weight:700;font-size:26px;fill:var(--white);}
  .bonus-text{font-family:"Roboto",sans-serif;font-style:italic;font-size:13px;fill:var(--white);}
  .activities-title{font-family:"Roboto Condensed",sans-serif;font-style:italic;font-weight:700;font-size:30px;fill:var(--sky);}
  .activity{font-family:"Roboto",sans-serif;font-style:italic;font-size:18px;fill:var(--ink);}
  .footer-text{font-family:"Roboto",sans-serif;font-style:italic;font-size:15px;fill:var(--white);}
</style>
</head>
<body>
<svg class="flyer" viewBox="0 0 882 1242" xmlns="http://www.w3.org/2000/svg">
  <defs>
    <linearGradient id="paperGrad" x1="0" y1="0" x2="1" y2="1">
      <stop offset="0" stop-color="#fafafa"/><stop offset="1" stop-color="var(--paper-shade)"/>
    </linearGradient>
    <linearGradient id="beachGrad" x1="0" y1="0" x2="0" y2="1">
      <stop offset="0" stop-color="#eaf6fc"/><stop offset=".4" stop-color="#a9cfdf"/>
      <stop offset=".55" stop-color="#e8eef0"/><stop offset="1" stop-color="#d9d4cc"/>
    </linearGradient>
    <linearGradient id="blueGrad" x1="0" y1="0" x2="0" y2="1">
      <stop offset="0" stop-color="#5ccdf6"/><stop offset="1" stop-color="var(--sky-deep)"/>
    </linearGradient>
    <linearGradient id="pillGrad" x1="0" y1="0" x2="0" y2="1">
      <stop offset="0" stop-color="#6fd6fa"/><stop offset="1" stop-color="#12a4e0"/>
    </linearGradient>
    <linearGradient id="panelGrad" x1="0" y1="0" x2="1" y2="1">
      <stop offset="0" stop-color="#3a3c40"/><stop offset="1" stop-color="#1d1f22"/>
    </linearGradient>
  </defs>

  <!-- page -->
  <rect class="page" width="882" height="1242" fill="url(#paperGrad)"/>

  <!-- hero photo -->
  <path class="hero-photo" role="img" aria-label="Woman meditating cross-legged on a sunny beach"
        d="M0,0 H560 V700 Q300,700 0,640 Z" fill="url(#beachGrad)"/>

  <!-- dark tagline panel with blue edge -->
  <path class="panel-edge" d="M478,0 H505 C560,200 565,420 640,575 L612,590 C540,430 540,200 478,0 Z" fill="var(--sky)"/>
  <path class="tagline-panel" d="M498,0 H882 V330 Q780,470 640,575 C570,420 560,200 498,0 Z" fill="url(#panelGrad)"/>

  <!-- blue swoosh -->
  <path class="swoosh-shadow" d="M0,880 Q160,955 420,938 Q700,910 882,640 V660 Q700,930 420,955 Q160,975 0,900 Z" fill="var(--ink)"/>
  <path class="swoosh" d="M0,640 Q260,720 520,670 Q720,620 882,320 V640 Q700,910 420,938 Q160,955 0,880 Z" fill="url(#blueGrad)"/>

  <!-- photo circles -->
  <circle cx="697" cy="401" r="152" fill="var(--ring)"/>
  <circle class="portrait-photo" role="img" aria-label="Portrait of the retreat host outdoors" cx="697" cy="401" r="138" fill="#8fb59a"/>
  <circle cx="534" cy="606" r="130" fill="var(--ring)"/>
  <circle class="yoga-photo" role="img" aria-label="Woman in a yoga pose with arms raised" cx="534" cy="606" r="118" fill="#f1f2f4" stroke="var(--sky)" stroke-width="3"/>
  <circle cx="716" cy="605" r="102" fill="var(--ring)"/>
  <circle class="sky-photo" role="img" aria-label="Woman with open arms facing a bright sky" cx="716" cy="605" r="91" fill="#cde6f5" stroke="var(--sky)" stroke-width="3"/>

  <!-- host name -->
  <text class="brand-name" x="70" y="140">Marnie Kovac</text>

  <!-- bonus badge -->
  <g class="bonus-badge">
    <circle cx="100" cy="545" r="70" fill="var(--panel)" stroke="var(--sky)" stroke-width="5"/>
    <text class="bonus-title" x="100" y="530" text-anchor="middle">BONUS</text>
    <text class="bonus-text" x="100" y="553" text-anchor="middle">30 minute reiki</text>
    <text class="bonus-text" x="100" y="571" text-anchor="middle">healing session</text>
  </g>

  <!-- tagline -->
  <text class="tagline" x="716" y="128" text-anchor="middle">Retreat</text>
  <text class="tagline" x="716" y="202" text-anchor="middle">into you</text>

  <!-- headline -->
  <text class="headline headline--dark" x="40" y="795">Blossomreach</text>
  <text class="headline headline--light" x="226" y="872">Within</text>

  <!-- call to action -->
  <rect class="cta-pill" x="46" y="988" width="484" height="56" rx="28" fill="url(#pillGrad)"/>
  <text class="cta-label" x="288" y="1028" text-anchor="middle">Join Our Upcoming Retreat</text>
  <text class="details" x="70" y="1080">Retreat will have fully catered raw food and juices. The retreat</text>
  <text class="details" x="70" y="1100">price includes all accomodation, meals and workshops.</text>
  <text class="event-info" x="70" y="1134">Date: [Date]   •   Time: [Time]</text>
  <text class="event-info" x="70" y="1156">Location: [Location]   •   Price: [Price]</text>

  <!-- divider -->
  <rect class="divider" x="574" y="890" width="8" height="290" fill="var(--sky)"/>

  <!-- activities -->
  <path class="activities-tab" d="M648,874 H882 V968 H648 L622,921 Z" fill="var(--sky)"/>
  <path d="M658,874 H882 V968 H658 L634,921 Z" fill="var(--panel)"/>
  <text class="activities-title" x="838" y="916" text-anchor="end">The Retreate</text>
  <text class="activities-title" x="838" y="948" text-anchor="end">Activities:</text>

  <g class="activity-list">
    <text class="activity" x="810" y="1016" text-anchor="end">Daily meditation</text>
    <circle cx="829" cy="1010" r="6" fill="var(--sky)"/>
    <text class="activity" x="810" y="1043" text-anchor="end">Ecstatic dance</text>
    <circle cx="829" cy="1037" r="6" fill="var(--sky)"/>
    <text class="activity" x="810" y="1071" text-anchor="end">Spiritual development</text>
    <circle cx="829" cy="1065" r="6" fill="var(--sky)"/>
    <text class="activity" x="810" y="1095" text-anchor="end">workshops on intuition</text>
    <text class="activity" x="810" y="1122" text-anchor="end">Energy healing</text>
    <circle cx="829" cy="1116" r="6" fill="var(--sky)"/>
    <text class="activity" x="810" y="1149" text-anchor="end">A reiki session</text>
    <circle cx="829" cy="1143" r="6" fill="var(--sky)"/>
  </g>

  <!-- footer -->
  <rect class="footer-bar" x="0" y="1180" width="882" height="62" fill="var(--sky)"/>
  <rect class="footer-label" x="0" y="1190" width="357" height="52" fill="var(--panel)"/>
  <text class="footer-text" x="60" y="1222">For further info please visit us at:</text>
  <text class="footer-text" x="372" y="1222" textLength="492" lengthAdjust="spacingAndGlyphs">www.marniekovac-studio.com | www.friendhub-sample.com/tuvelanook</text>
</svg>
</body>
</html>
```